Coffee cup sleeve design

Need a coffee cup sleeve designed. I've included our logo as well as some inspiration photos and the template for the sleeve. Would like to add a very small 8pt "Lamentations 3:22-23" on back too.

Colors

Designer to choose only greyscale colors for use in the design.

```html
<!DOCTYPE html>
<html lang="en">
<head>
<meta charset="utf-8">
<title>Ironwood Cafe – Cup Sleeve</title>
<link href="https://fonts.googleapis.com/css2?family=Marcellus&display=swap" rel="stylesheet">
<style>
  :root {
    --ink: #111111;
    --paper: #ffffff;
    --mid: #8a8a8a;
    --backdrop: #efe6e7;
  }
  * { margin: 0; padding: 0; box-sizing: border-box; }
  html, body { width: 759px; height: 1200px; overflow: hidden; }
  body { background: var(--backdrop); position: relative; font-family: "Marcellus", serif; }

  .pattern-swatch {
    position: absolute; left: 0; top: 0; width: 759px; height: 372px;
    background: repeating-linear-gradient(60deg, #3a3a3a 0 3px, #d8d8d8 3px 6px);
  }

  .sleeve {
    position: absolute; top: 416px; width: 310px; height: 167px;
    background: var(--paper);
    box-shadow: -8px 10px 14px rgba(0,0,0,0.28);
    display: flex; flex-direction: column;
  }
  .sleeve--front { left: 39px; }
  .sleeve--back { left: 405px; }

  .name-band {
    height: 23px; display: flex; justify-content: space-around; align-items: center;
    font-size: 6.6px; letter-spacing: 0.1px; color: var(--ink);
    border-top: 2px solid var(--ink);
  }
  .name-band--bottom { border-top: none; border-bottom: 2px solid var(--ink); }

  .burst {
    position: relative; flex: 1; border-top: 3px solid var(--ink); border-bottom: 3px solid var(--ink);
    background: repeating-linear-gradient(0deg, var(--ink) 0 4px, var(--paper) 4px 8px);
    overflow: hidden;
  }
  .sleeve--back .burst {
    background:
      radial-gradient(ellipse 60px 56px at 50% 50%, var(--paper) 70%, rgba(255,255,255,0) 100%),
      repeating-linear-gradient(0deg, var(--ink) 0 4px, var(--paper) 4px 8px);
  }

  .emblem {
    position: absolute; left: 50%; top: 50%; width: 100px; height: 100px;
    transform: translate(-50%, -50%);
    background: var(--paper); border: 3px solid var(--ink); border-radius: 50%;
    display: flex; align-items: center; justify-content: center;
    font-size: 11px; color: var(--ink); text-align: center; line-height: 1.2;
  }

  .cut-line { position: absolute; left: 0; top: 0; pointer-events: none; }
</style>
</head>
<body>
  <div class="pattern-swatch" role="img" aria-label="Black and white interlaced striped triangle pattern"></div>

  <section class="sleeve sleeve--front">
    <div class="name-band"><span>IRONWOOD CAFE</span><span>IRONWOOD CAFE</span><span>IRONWOOD CAFE</span><span>IRONWOOD CAFE</span></div>
    <div class="burst" role="img" aria-label="Black and white radiating chevron stripe pattern">
      <div class="emblem">IRONWOOD<br>CAFE</div>
    </div>
    <div class="name-band name-band--bottom"><span>IRONWOOD CAFE</span><span>IRONWOOD CAFE</span><span>IRONWOOD CAFE</span><span>IRONWOOD CAFE</span></div>
  </section>

  <section class="sleeve sleeve--back">
    <div class="name-band"><span>IRONWOOD CAFE</span><span>IRONWOOD CAFE</span><span>IRONWOOD CAFE</span><span>IRONWOOD CAFE</span></div>
    <div class="burst" role="img" aria-label="Black and white radiating chevron stripe pattern with open white center"></div>
    <div class="name-band name-band--bottom"><span>IRONWOOD CAFE</span><span>IRONWOOD CAFE</span><span>IRONWOOD CAFE</span><span>IRONWOOD CAFE</span></div>
    <svg class="cut-line" width="310" height="167" viewBox="0 0 310 167">
      <line x1="192" y1="4" x2="117" y2="163" stroke="#111111" stroke-width="3"/>
      <line x1="192" y1="4" x2="117" y2="163" stroke="#ffffff" stroke-width="0.8" stroke-dasharray="3 3"/>
    </svg>
  </section>
</body>
</html>
```